Velmora Grove Club Postcard Design

Need a postcard for this business. Go to velmoragroveclub.com to see the product we are selling. Here's another good postcard you can sample. https://www.rowanpilsbydesign.com/?lightbox=dataItem-qz4tunal
Another one: http://blog.tranquet.com/postcard-examples-from-popular-startups/

```html
<!DOCTYPE html>
<html lang="en">
<head>
<meta charset="utf-8">
<title>Velmora Grove Club Postcard</title>
<link rel="stylesheet" href="https://fonts.googleapis.com/css2?family=Rokkitt:wght@500;600&family=Poppins:wght@400;500;600;700&family=Lobster+Two:wght@700&display=swap">
<style>
  :root {
    --page: #e8e8e6;
    --white: #ffffff;
    --green: #6aa84a;
    --green-dark: #5a9a3c;
    --teal: #5bb8c4;
    --teal-light: #a9dbe1;
    --brown: #b06a5a;
    --sage: #a6bd9a;
    --orange: #f0612a;
    --ink: #1e1e1e;
    --black: #0e0e0e;
    --stamp: #3aa5d8;
    --dots: #9a9a9a;
  }
  * { box-sizing: border-box; margin: 0; padding: 0; }
  html, body { width: 1200px; height: 1200px; overflow: hidden; background: var(--page); }
  body { position: relative; font-family: "Poppins", sans-serif; }

  .postcard { position: absolute; left: 236px; width: 728px; height: 519px; background: var(--white); overflow: hidden; box-shadow: 0 3px 10px rgba(0,0,0,.18); }
  .postcard--front { top: 48px; }
  .postcard--back { top: 626px; }
  .layer { position: absolute; inset: 0; }
  .abs { position: absolute; }

  /* FRONT */
  .title-banner { left: 0; top: 28px; width: 338px; height: 93px; background: var(--green); color: var(--white); font-family: "Rokkitt", serif; font-weight: 600; text-align: center; padding-right: 56px; }
  .title-banner .line-1 { font-size: 29px; line-height: 1; margin-top: 11px; letter-spacing: .5px; white-space: nowrap; }
  .title-banner .line-2 { font-size: 46px; line-height: 1; margin-top: 3px; }
  .title-banner .paw { display: inline-block; width: 14px; height: 14px; border-radius: 50%; background: var(--white); vertical-align: middle; margin: 0 8px; }

  .brand-seal { width: 126px; height: 126px; border-radius: 50%; background: var(--white); border: 3px solid var(--ink); display: flex; align-items: center; justify-content: center; text-align: center; font-family: "Poppins", sans-serif; font-weight: 600; font-size: 13px; line-height: 1.2; color: var(--ink); padding: 16px; }
  .brand-seal--front { left: 328px; top: 5px; }
  .brand-seal--back { left: 15px; top: 7px; width: 88px; height: 88px; font-size: 10px; padding: 10px; }

  .price-pill { left: 464px; top: 60px; width: 147px; height: 41px; border-radius: 21px; background: var(--brown); border: 2px solid #e8c7bf; color: var(--white); font-weight: 700; font-size: 27px; line-height: 37px; text-align: center; }
  .price-note { left: 464px; top: 103px; width: 147px; text-align: center; color: var(--white); font-size: 15px; font-weight: 500; }
  .billing-note { left: 452px; top: 150px; width: 170px; text-align: center; color: var(--white); font-size: 14.5px; line-height: 1.32; }

  .intro { left: 180px; top: 150px; width: 245px; font-size: 15.5px; line-height: 1.36; color: var(--ink); }
  .join { left: 262px; top: 270px; font-family: "Lobster Two", cursive; font-weight: 700; font-size: 40px; color: var(--brown); }

  .photo { display: block; }
  .photo--dogs { left: 11px; top: 165px; width: 158px; height: 340px; border-radius: 40px 40px 10px 10px; background: linear-gradient(160deg, #3a2a22 0%, #8b6a4e 45%, #d6b58e 75%, #e7c9a8 100%); }
  .photo--treats { left: 503px; top: 225px; width: 88px; height: 115px; border-radius: 10px; background: linear-gradient(100deg, #7a3c1f, #b46b3d 55%, #8a4a26); }

  .feature { width: 120px; height: 120px; border-radius: 50%; background: var(--white); border: 3px solid var(--green); display: flex; align-items: center; justify-content: center; }
  .feature__art { width: 72px; height: 66px; border-radius: 50%; }
  .feature--joy { left: 205px; top: 340px; }
  .feature--joy .feature__art { background: linear-gradient(#f1e3d6, #b86a44); }
  .feature--cattle { left: 340px; top: 340px; }
  .feature--cattle .feature__art { background: #1b1b1b; border-radius: 30% 40% 30% 40%; }
  .feature--ship { left: 487px; top: 340px; }
  .feature--ship .feature__art { background: linear-gradient(#e3b774, #b5833e); border-radius: 8px; }

  .feature-label { top: 470px; width: 136px; text-align: center; color: var(--white); font-size: 12.5px; line-height: 1.3; font-weight: 500; }
  .feature-label--joy { left: 197px; }
  .feature-label--cattle { left: 332px; }
  .feature-label--ship { left: 479px; }

  .offer-strip { left: 633px; top: 0; width: 95px; height: 519px; background: var(--brown); }
  .offer-rot { position: absolute; width: 519px; height: 95px; left: calc(95px / 2 - 519px / 2); top: calc(519px / 2 - 95px / 2); transform: rotate(-90deg); }
  .offer-save { left: 34px; top: 8px; font-size: 46px; font-weight: 600; color: var(--white); line-height: 1; letter-spacing: 1px; }
  .offer-terms { left: 282px; top: 9px; font-size: 13.5px; line-height: 1.3; color: var(--white); font-weight: 500; }
  .offer-url { left: 49px; top: 62px; width: 380px; height: 40px; background: var(--white); border-radius: 20px; color: var(--green-dark); font-weight: 600; font-size: 19px; line-height: 34px; text-align: center; letter-spacing: .3px; }

  /* BACK */
  .back-title { left: 100px; top: 22px; width: 327px; height: 34px; background: var(--teal); color: var(--white); font-family: "Rokkitt", serif; font-weight: 600; font-size: 25px; line-height: 34px; padding-left: 14px; white-space: nowrap; }
  .back-sub { left: 100px; top: 58px; width: 345px; height: 28px; background: var(--orange); color: var(--white); font-size: 14.5px; font-weight: 500; line-height: 28px; padding-left: 12px; clip-path: polygon(0 0, 100% 0, 96% 100%, 0 100%); }

  .benefits { left: 18px; top: 118px; width: 420px; list-style: none; color: var(--white); font-size: 15px; line-height: 20.8px; font-weight: 500; }
  .benefits li { position: relative; padding-left: 25px; white-space: nowrap; }
  .benefits svg { position: absolute; left: 0; top: 3px; width: 19px; height: 16px; }

  .stamp-box { left: 611px; top: 16px; width: 100px; height: 109px; border: 2px solid var(--stamp); }
  .address-line { height: 0; border-top: 2px dotted var(--dots); }

  .quote-art { left: 18px; top: 392px; width: 100px; height: 100px; border-radius: 50%; background: radial-gradient(circle at 50% 60%, #c8996b 0 28%, #ffffff 30%); }
  .quote-head { left: 122px; top: 386px; font-size: 15.5px; font-weight: 500; color: var(--orange); }
  .quote-body { left: 122px; top: 408px; width: 236px; font-size: 10.2px; line-height: 1.33; color: var(--ink); }

  .photo--lab { left: 368px; top: 333px; width: 190px; height: 186px; border-radius: 90px 90px 0 0; background: linear-gradient(150deg, #4a3226 0%, #2a1c16 50%, #c0607a 72%, #9a4e2b 100%); }
  .back-url { left: 498px; top: 490px; width: 240px; height: 34px; border-radius: 17px 0 0 0; background: var(--teal); color: var(--white); font-size: 12.5px; font-weight: 500; line-height: 30px; padding-left: 26px; }
</style>
</head>
<body>

<section class="postcard postcard--front" aria-label="Postcard front">
  <svg class="layer" viewBox="0 0 728 519" aria-hidden="true">
    <rect x="0" y="0" width="728" height="519" fill="var(--teal)"/>
    <path d="M0,0 H345 C430,60 478,200 470,300 C462,400 430,460 395,519 H0 Z" fill="var(--teal-light)"/>
    <path d="M0,0 H330 C410,60 455,200 448,300 C441,400 410,460 375,519 H0 Z" fill="var(--white)"/>
    <path d="M198,448 H633 V506 H226 A29,29 0 0 1 198,477 Z" fill="var(--sage)"/>
    <rect x="0" y="506" width="633" height="13" fill="var(--teal)"/>
  </svg>

  <div class="abs title-banner">
    <div class="line-1">VELMORA GROVE</div>
    <div class="line-2"><span class="paw"></span>CLUB<span class="paw"></span></div>
  </div>
  <div class="abs brand-seal brand-seal--front">Velmora Grove Club</div>

  <div class="abs price-pill">$12.95</div>
  <div class="abs price-note">a month!</div>
  <p class="abs billing-note">You will be charged monthly. You can cancel anytime.</p>

  <div class="abs photo photo--dogs" role="img" aria-label="Photo of a large tricolour dog sitting beside a pug wearing sunglasses and a bandana"></div>
  <p class="abs intro">is a monthly subscription club that offers the most popular dog treats at intervals that fit your dog's chewing appetite.</p>
  <div class="abs join">Join Us</div>
  <div class="abs photo photo--treats" role="img" aria-label="Photo of three bully sticks"></div>

  <div class="abs feature feature--joy"><div class="feature__art" role="img" aria-label="Illustration of a happy small dog with a ribbon badge"></div></div>
  <div class="abs feature feature--cattle"><div class="feature__art" role="img" aria-label="Illustration of a cow silhouette marked premium quality"></div></div>
  <div class="abs feature feature--ship"><div class="feature__art" role="img" aria-label="Illustration of a cardboard shipping box"></div></div>

  <div class="abs feature-label feature-label--joy">Doggy Joy<br>GUARANTEE!</div>
  <div class="abs feature-label feature-label--cattle">Sourced From<br>Free Range Cattle</div>
  <div class="abs feature-label feature-label--ship">Shipped to<br>Your Doorstep!</div>

  <aside class="abs offer-strip">
    <div class="offer-rot">
      <div class="abs offer-save">SAVE 50%</div>
      <div class="abs offer-terms">on Your First Month<br>by Sign Up for Subscription</div>
      <div class="abs offer-url">www.velmoragroveclub.com</div>
    </div>
  </aside>
</section>

<section class="postcard postcard--back" aria-label="Postcard back">
  <svg class="layer" viewBox="0 0 728 519" aria-hidden="true">
    <path d="M0,0 H326 C410,20 468,100 468,200 V375 L430,519 H0 Z" fill="var(--sage)"/>
    <path d="M0,0 H296 C380,20 440,100 440,200 V375 H0 Z" fill="var(--black)"/>
  </svg>

  <div class="abs brand-seal brand-seal--back">Velmora Grove Club</div>
  <div class="abs back-title">VELMORA GROVE CLUB</div>
  <div class="abs back-sub">TOP QUALITY &amp; HEALTHY BULL STICKS</div>

  <ul class="abs benefits">
    <li><svg viewBox="0 0 19 16"><circle cx="8" cy="8.5" r="6.5" fill="none" stroke="var(--orange)" stroke-width="2"/><path d="M4.5 8 L8 11.5 L17 2" fill="none" stroke="var(--orange)" stroke-width="2.4" stroke-linecap="round"/></svg>USDA Certified, Inspected &amp; Approved</li>
    <li><svg viewBox="0 0 19 16"><circle cx="8" cy="8.5" r="6.5" fill="none" stroke="var(--orange)" stroke-width="2"/><path d="M4.5 8 L8 11.5 L17 2" fill="none" stroke="var(--orange)" stroke-width="2.4" stroke-linecap="round"/></svg>100% Digestible Safely Passes<br>through your dog</li>
    <li><svg viewBox="0 0 19 16"><circle cx="8" cy="8.5" r="6.5" fill="none" stroke="var(--orange)" stroke-width="2"/><path d="M4.5 8 L8 11.5 L17 2" fill="none" stroke="var(--orange)" stroke-width="2.4" stroke-linecap="round"/></svg>Slowly oven baked 100% Natural beef pizzle.</li>
    <li><svg viewBox="0 0 19 16"><circle cx="8" cy="8.5" r="6.5" fill="none" stroke="var(--orange)" stroke-width="2"/><path d="M4.5 8 L8 11.5 L17 2" fill="none" stroke="var(--orange)" stroke-width="2.4" stroke-linecap="round"/></svg>No chemicals used</li>
    <li><svg viewBox="0 0 19 16"><circle cx="8" cy="8.5" r="6.5" fill="none" stroke="var(--orange)" stroke-width="2"/><path d="M4.5 8 L8 11.5 L17 2" fill="none" stroke="var(--orange)" stroke-width="2.4" stroke-linecap="round"/></svg>Dissolves into safe, soft form.</li>
    <li><svg viewBox="0 0 19 16"><circle cx="8" cy="8.5" r="6.5" fill="none" stroke="var(--orange)" stroke-width="2"/><path d="M4.5 8 L8 11.5 L17 2" fill="none" stroke="var(--orange)" stroke-width="2.4" stroke-linecap="round"/></svg>Naturally Contains glucosamine &amp;<br>chondroitin for joint support</li>
    <li>Promotes Oral Health</li>
    <li><svg viewBox="0 0 19 16"><circle cx="8" cy="8.5" r="6.5" fill="none" stroke="var(--orange)" stroke-width="2"/><path d="M4.5 8 L8 11.5 L17 2" fill="none" stroke="var(--orange)" stroke-width="2.4" stroke-linecap="round"/></svg>Provides Stress Relief</li>
    <li><svg viewBox="0 0 19 16"><circle cx="8" cy="8.5" r="6.5" fill="none" stroke="var(--orange)" stroke-width="2"/><path d="M4.5 8 L8 11.5 L17 2" fill="none" stroke="var(--orange)" stroke-width="2.4" stroke-linecap="round"/></svg>High in Protein, Low in Fat</li>
  </ul>

  <div class="abs stamp-box" aria-label="Stamp area"></div>
  <div class="abs address-line" style="left:481px;top:167px;width:230px"></div>
  <div class="abs address-line" style="left:481px;top:201px;width:230px"></div>
  <div class="abs address-line" style="left:481px;top:236px;width:230px"></div>
  <div class="abs address-line" style="left:503px;top:270px;width:208px"></div>
  <div class="abs address-line" style="left:514px;top:305px;width:197px"></div>
  <div class="abs address-line" style="left:552px;top:340px;width:159px"></div>

  <div class="abs quote-art" role="img" aria-label="White paw print framing a small photo of a dog"></div>
  <div class="abs quote-head">Slowly but surely</div>
  <p class="abs quote-body">My little Pepper is 20 pounds but has the appetite of a much bigger dog. I'm always worried that she eats her food way too fast. A friend suggested bully sticks and i found this club. The cool thing about the bully sticks is that she takes her sweet time. ~Maren T.</p>

  <div class="abs photo photo--lab" role="img" aria-label="Photo of a chocolate labrador licking its nose beside bully sticks"></div>
  <div class="abs back-url">www.velmoragroveclub.com</div>
</section>

</body>
</html>
```